ORV Holding

ORV holding is located in the UAE. In the company, there are several departments covering Hospitality management, Facility Management, interior design and Construction.

The logo should not include the name holding, Just ORV.

Needed Items:

(1) Logo.
(2) Business Card.
(3) Letterhead
(4) Envelope
(5) cd cover
(6) email signature
Updates

The previous brief was misplaced with another competition. Current update is the final.

Target Market(s)

Collaboration with international high end firms.

Industry/Entity Type

Business

Requirements
Must have
• COLOR PREFERENCE Maximum 2 colors, preferably mono-color with different shades.
Nice to have
• Elegant, luxurious, and minimalistic.

```html
<!DOCTYPE html>
<html lang="en">
<head>
<meta charset="utf-8">
<title>ORV Holding – Business Card</title>
<link rel="stylesheet" href="https://fonts.googleapis.com/css2?family=Montserrat:wght@500;700&family=Roboto:wght@400&family=Cairo:wght@700&display=swap">
<style>
  :root {
    --backdrop: #2a2b2e;
    --brand-blue: #5676b2;
    --brand-blue-light: #7f9bca;
    --ink-grey: #8a8a8a;
    --ink-dark: #6e6e6e;
    --rule: #9a9a9a;
    --paper: #ffffff;
  }
  * { box-sizing: border-box; margin: 0; padding: 0; }
  html, body { width: 1200px; height: 929px; overflow: hidden; }
  body { background: var(--backdrop); position: relative; font-family: "Roboto", sans-serif; }

  .card {
    position: absolute; left: 280px; width: 640px; height: 366px;
    border-radius: 18px; overflow: hidden;
  }
  .card--front {
    top: 62px;
    background: linear-gradient(120deg, var(--brand-blue) 0%, var(--brand-blue-light) 70%, #6f8dc2 100%);
  }
  .card--back { top: 500px; background: var(--paper); }

  .lockup { position: absolute; display: flex; align-items: center; }
  .lockup__square { flex: none; }
  .lockup__words { display: flex; flex-direction: column; line-height: 1; font-weight: 700; white-space: nowrap; }
  .lockup__latin { font-family: "Montserrat", sans-serif; letter-spacing: 1px; }
  .lockup__arabic { font-family: "Cairo", sans-serif; direction: rtl; text-align: left; margin-top: 4px; }

  .card--front .lockup { left: 110px; top: 124px; gap: 20px; }
  .card--front .lockup__square { width: 118px; height: 118px; background: var(--paper); }
  .card--front .lockup__words { color: var(--paper); }
  .card--front .lockup__latin { font-size: 40px; }
  .card--front .lockup__arabic { font-size: 34px; }

  .card--back .lockup { left: 36px; top: 160px; gap: 14px; }
  .card--back .lockup__square { width: 92px; height: 92px; background: var(--brand-blue); }
  .card--back .lockup__words { color: var(--ink-grey); }
  .card--back .lockup__latin { font-size: 27px; letter-spacing: .5px; }
  .card--back .lockup__arabic { font-size: 24px; }

  .divider { position: absolute; left: 400px; width: 1.5px; background: var(--rule); }
  .divider--short { top: 100px; height: 40px; }
  .divider--long { top: 156px; height: 130px; }

  .contact { position: absolute; left: 418px; top: 92px; color: var(--ink-grey); white-space: nowrap; }
  .contact__name { font-family: "Montserrat", sans-serif; font-weight: 700; font-size: 18px; color: var(--brand-blue); letter-spacing: .3px; }
  .contact__role { font-family: "Montserrat", sans-serif; font-weight: 500; font-size: 14px; color: var(--ink-dark); margin-top: 2px; }
  .contact__address { font-size: 13.5px; line-height: 1.35; margin-top: 14px; }
  .contact__list { list-style: none; margin-top: 10px; font-size: 13.5px; line-height: 1.6; }
  .contact__list li { display: flex; align-items: center; gap: 8px; }
  .contact__list svg { width: 14px; height: 14px; flex: none; }
</style>
</head>
<body>

<section class="card card--front">
  <div class="lockup">
    <div class="lockup__square"></div>
    <div class="lockup__words">
      <span class="lockup__latin">ORV HOLDING</span>
      <span class="lockup__arabic">أورف القابضة</span>
    </div>
  </div>
</section>

<section class="card card--back">
  <div class="lockup">
    <div class="lockup__square"></div>
    <div class="lockup__words">
      <span class="lockup__latin">ORV HOLDING</span>
      <span class="lockup__arabic">أورف القابضة</span>
    </div>
  </div>

  <div class="divider divider--short"></div>
  <div class="divider divider--long"></div>

  <div class="contact">
    <p class="contact__name">KARIM HADDAD</p>
    <p class="contact__role">Managing Director</p>
    <p class="contact__address">14 Harbour View Road,<br>Marina District, AD 2W4</p>
    <ul class="contact__list">
      <li>
        <svg viewBox="0 0 24 24" fill="var(--brand-blue)"><path d="M6.6 10.8a15 15 0 0 0 6.6 6.6l2.2-2.2a1 1 0 0 1 1-.25 11.4 11.4 0 0 0 3.6.57 1 1 0 0 1 1 1V20a1 1 0 0 1-1 1A17 17 0 0 1 3 4a1 1 0 0 1 1-1h3.5a1 1 0 0 1 1 1c0 1.25.2 2.45.57 3.57a1 1 0 0 1-.25 1z"/></svg>
        +97125550148
      </li>
      <li>
        <svg viewBox="0 0 24 24" fill="none" stroke="var(--brand-blue)" stroke-width="2.2"><rect x="3" y="5" width="18" height="14"/><path d="M3 5l9 8 9-8"/></svg>
        info@orvholding.ae
      </li>
      <li>
        <svg viewBox="0 0 24 24" fill="none" stroke="var(--brand-blue)" stroke-width="2"><circle cx="12" cy="12" r="9"/><path d="M3 12h18M12 3c3 3 3 15 0 18M12 3c-3 3-3 15 0 18"/></svg>
        www.orvholding.ae
      </li>
    </ul>
  </div>
</section>

</body>
</html>
```